LWB Homepage Banner

I would like a banner that uses/interprets the existing graphic on the www.leonwardbriggs.example homepage.

Target Market(s)

Business professionals across a variety of industries and sectors.

Requirements
Must have
• Must incorporate all the words and relationships of the existing image (file attached). I am seeking a professional and clean interpretation of the image.
• Must consider the look and feel of the banner on the following page: http://www.leonwardbriggs.example/pathways-in-coastal-crm/ (file attached)
• Must include the LWB logo in a similar style to the banner on the Pathways in Coastal CRM page (file attached).
Nice to have
• Feel free to add background/foreground graphics.
• I like the design idea of "bio-mechanical" applied to a professional services/business industry.
• The overall image must display a "business-technology-people-change" balance.
Should not have
• Should not be a direct replication of the existing graphic but must contain all the words and relationships.

```html
<!DOCTYPE html>
<html lang="en">
<head>
<meta charset="utf-8">
<title>LWB Homepage Banner</title>
<link rel="stylesheet" href="https://fonts.googleapis.com/css2?family=Arimo:wght@400;700&display=swap">
<style>
  :root {
    --brand-dark: #245ca8;
    --brand-mid: #6389c2;
    --brand-light: #a0c8fa;
    --ink-white: #ffffff;
    --paper: #ffffff;
  }
  html, body {
    margin: 0;
    padding: 0;
    width: 1200px;
    height: 1000px;
    overflow: hidden;
    background: var(--paper);
  }
  .banner {
    display: block;
    width: 1200px;
    height: 1000px;
    font-family: "Arimo", Arial, sans-serif;
  }
  .brand-name { fill: var(--brand-dark); font-weight: 700; }
  .rule { fill: var(--brand-dark); }
  .domain-box { fill: var(--brand-mid); }
  .role-box { fill: var(--brand-mid); }
  .domain-link { fill: var(--brand-dark); }
  .box-label { fill: var(--ink-white); font-weight: 700; font-size: 15px; text-anchor: middle; }
  .risk-band { fill: var(--brand-light); }
  .risk-title { fill: var(--brand-dark); font-weight: 700; font-size: 19px; }
  .risk-sub { fill: var(--brand-dark); font-size: 15px; }
  .hub-halo { fill: var(--brand-light); }
  .hub-core { fill: var(--brand-mid); }
  .hub-title { fill: var(--ink-white); font-weight: 700; font-size: 19px; text-anchor: middle; }
  .hub-sub { fill: var(--ink-white); font-size: 15px; text-anchor: middle; }
  .cycle-link-outer { stroke: var(--brand-mid); stroke-width: 16; }
  .cycle-link-inner { stroke: var(--brand-dark); stroke-width: 6; }
  .stage-ring { fill: var(--brand-mid); }
  .stage-core { fill: var(--brand-dark); }
  .stage-label { fill: var(--ink-white); font-weight: 700; font-size: 15px; text-anchor: middle; }
  .exchange-arrow { stroke: var(--brand-dark); stroke-width: 2; fill: none; }
  .arrow-head { fill: var(--brand-dark); }
</style>
</head>
<body>
<svg class="banner" viewBox="0 0 1200 1000" xmlns="http://www.w3.org/2000/svg">
  <defs>
    <g id="stage">
      <circle class="stage-ring" r="73"/>
      <circle class="stage-core" r="60"/>
    </g>
  </defs>

  <!-- Brand header -->
  <g class="brand">
    <text class="brand-name" x="20" y="228" font-size="52">LWB</text>
    <text class="brand-name" x="150" y="214" font-size="20" letter-spacing="1">LEON WARD BRIGGS</text>
    <text class="brand-name" x="150" y="231" font-size="11" letter-spacing="4">ADVISORY</text>
    <rect class="rule" x="378" y="199" width="737" height="8"/>
  </g>

  <!-- Enterprise domains -->
  <g class="domains">
    <rect class="domain-link" x="280" y="288" width="640" height="9"/>
    <rect class="domain-box" x="117" y="264" width="165" height="57"/>
    <text class="box-label" x="199" y="297">Enterprise Strategy</text>
    <rect class="domain-box" x="317" y="264" width="165" height="57"/>
    <text class="box-label" x="399" y="298">Enterprise Software</text>
    <rect class="domain-box" x="516" y="264" width="165" height="57"/>
    <text class="box-label" x="598" y="298">Enterprise Hardware</text>
    <rect class="domain-box" x="715" y="264" width="165" height="57"/>
    <text class="box-label" x="797" y="297">Enterprise Networks</text>
    <rect class="domain-box" x="915" y="264" width="165" height="57"/>
    <text class="box-label" x="997" y="296">Enterprise Services</text>
  </g>

  <!-- Risk band -->
  <rect class="risk-band" x="16" y="341" width="1132" height="52"/>
  <text class="risk-title" x="25" y="365">Procurement Risk</text>
  <text class="risk-sub" x="55" y="383">The right partner</text>
  <text class="risk-title" x="1136" y="366" text-anchor="end">Business Risk</text>
  <text class="risk-sub" x="1130" y="383" text-anchor="end">The right outcome</text>

  <!-- Independence hub -->
  <ellipse class="hub-halo" cx="600" cy="402" rx="171" ry="53"/>
  <ellipse class="hub-core" cx="600" cy="398" rx="158" ry="42"/>
  <text class="hub-title" x="600" y="393">Independence Risk</text>
  <text class="hub-sub" x="600" y="415">The right technology framework</text>

  <!-- Exchange arrow -->
  <line class="exchange-arrow" x1="500" y1="463" x2="694" y2="463"/>
  <path class="arrow-head" d="M492 463 L524 456 L516 463 L524 470 Z"/>
  <path class="arrow-head" d="M702 463 L670 456 L678 463 L670 470 Z"/>

  <!-- Procurement cycle -->
  <g class="cycle cycle-procurement">
    <g class="cycle-links">
      <path class="cycle-link-outer" d="M299 406 L413 510 L378 661 L218 657 L180 511 Z" fill="none"/>
      <path class="cycle-link-inner" d="M299 406 L413 510 L378 661 L218 657 L180 511 Z" fill="none"/>
    </g>
    <use href="#stage" x="299" y="406"/>
    <text class="stage-label" x="299" y="411">Evaluate</text>
    <use href="#stage" x="413" y="510"/>
    <text class="stage-label" x="413" y="515">Procure</text>
    <use href="#stage" x="378" y="661"/>
    <text class="stage-label" x="378" y="666">Impliment</text>
    <use href="#stage" x="218" y="657"/>
    <text class="stage-label" x="218" y="662">Maintain</text>
    <use href="#stage" x="180" y="511"/>
    <text class="stage-label" x="180" y="516">Upgrade</text>
  </g>

  <!-- Business cycle -->
  <g class="cycle cycle-business">
    <g class="cycle-links">
      <path class="cycle-link-outer" d="M899 408 L1013 511 L978 660 L818 661 L780 510 Z" fill="none"/>
      <path class="cycle-link-inner" d="M899 408 L1013 511 L978 660 L818 661 L780 510 Z" fill="none"/>
    </g>
    <use href="#stage" x="899" y="408"/>
    <text class="stage-label" x="899" y="413">Change</text>
    <use href="#stage" x="1013" y="511"/>
    <text class="stage-label" x="1013" y="516">Communicate</text>
    <use href="#stage" x="978" y="660"/>
    <text class="stage-label" x="978" y="665">Process</text>
    <use href="#stage" x="818" y="661"/>
    <text class="stage-label" x="818" y="666">Impliment</text>
    <use href="#stage" x="780" y="510"/>
    <text class="stage-label" x="780" y="515">Govern</text>
  </g>

  <!-- People roles -->
  <g class="roles">
    <rect class="role-box" x="316" y="750" width="166" height="57"/>
    <text class="box-label" x="399" y="783">Analysts</text>
    <rect class="role-box" x="516" y="750" width="165" height="57"/>
    <text class="box-label" x="598" y="784">Advisors</text>
    <rect class="role-box" x="715" y="750" width="165" height="57"/>
    <text class="box-label" x="798" y="774">Programme</text>
    <text class="box-label" x="798" y="794">Managers</text>
  </g>
</svg>
</body>
</html>
```